Business Card for Fashion House

We need a business card design for our personalize fashion service for our customers. the business card should reflect reliability, luxury and creativity.
The brand Vastrelle is extracted from "Vibrant Estrella"; Vastrelle provides fashion designs sprinkled with luxury and style tailored for our elite clients character profile.
Vastrelle is created for those who embody class and elegance with a passion for style.
Target Market(s)
Affluent Customers
Industry/Entity Type
Fashion
Contact Information for Business Card
Noura Al Hashimi
Fashion Designer
Telephone: +971 5550192
Mobile +971 555073
Emal q@k.example
Website www.vastrelle.example
Social Media Youtube g+ Facebook Instagram Pin /vastrelle
Font styles to use
Other font styles liked:
- Audrey provided
Look and feel
Each slider illustrates characteristics of the customer's brand and the style your logo design should communicate.

```html
<!DOCTYPE html>
<html lang="en">
<head>
<meta charset="utf-8">
<title>Vastrelle – Business Card</title>
<link rel="stylesheet" href="https://fonts.googleapis.com/css2?family=Federo&family=Roboto:wght@400&display=swap">
<style>
  :root {
    --page-bg: #d9d2ca;
    --card-top: #efebe6;
    --card-bottom: #e4ded7;
    --card-edge: #f7f4f0;
    --ink: #1e1e1e;
    --ink-soft: #2a2a2a;
  }
  html, body {
    margin: 0;
    padding: 0;
    width: 1200px;
    height: 1054px;
    overflow: hidden;
    background: var(--page-bg);
  }
  .canvas {
    position: relative;
    width: 1200px;
    height: 1054px;
  }
  .card {
    position: absolute;
    left: 100px;
    top: 224px;
    width: 1000px;
    height: 605px;
    background: linear-gradient(160deg, var(--card-top), var(--card-bottom));
    border: 1.5px solid var(--card-edge);
    box-shadow: 0 10px 30px rgba(60, 45, 35, 0.18);
    color: var(--ink);
  }
  .holder-name {
    position: absolute;
    top: 120px;
    left: 0;
    width: 100%;
    text-align: center;
    font-family: "Federo", sans-serif;
    font-size: 42px;
    letter-spacing: 0.5px;
    margin: 0;
  }
  .holder-role {
    position: absolute;
    top: 178px;
    left: 0;
    width: 100%;
    text-align: center;
    font-family: "Roboto", sans-serif;
    font-size: 21px;
    color: var(--ink-soft);
    margin: 0;
  }
  .contact-icons {
    position: absolute;
    top: 259px;
    left: 50%;
    transform: translateX(-50%);
    display: flex;
    gap: 14px;
  }
  .contact-icons svg {
    width: 28px;
    height: 28px;
  }
  .contact-list {
    position: absolute;
    top: 304px;
    left: 0;
    width: 100%;
    margin: 0;
    padding: 0;
    list-style: none;
    text-align: center;
    font-family: "Roboto", sans-serif;
    font-size: 25px;
    line-height: 34px;
  }
  .divider {
    position: absolute;
    top: 500px;
    left: 55px;
    width: 894px;
    height: 2px;
    background: var(--ink);
  }
  .social-row {
    position: absolute;
    top: 530px;
    left: 0;
    width: 100%;
    display: flex;
    justify-content: center;
    align-items: center;
    gap: 12px;
    font-family: "Roboto", sans-serif;
    font-size: 28px;
  }
  .social-dot {
    width: 26px;
    height: 26px;
    border-radius: 50%;
    background: var(--ink);
  }
</style>
</head>
<body>
<main class="canvas">
  <section class="card">
    <h1 class="holder-name">Noura Al Hashimi</h1>
    <p class="holder-role">Fashion Designer</p>

    <div class="contact-icons" aria-hidden="true">
      <svg viewBox="0 0 24 24" fill="none" stroke="#1e1e1e" stroke-width="1.6">
        <circle cx="12" cy="12" r="10"/>
        <path d="M8.5 7.2c-.8.4-1.3 1.3-1 2.4.9 3 3 5.3 6 6.6 1 .4 2 0 2.5-.8l.4-.7-2.1-1.4-1 .8c-1.3-.6-2.4-1.7-3-3l.8-1-1.3-2.2z" fill="#1e1e1e" stroke="none"/>
      </svg>
      <svg viewBox="0 0 24 24" fill="none" stroke="#1e1e1e" stroke-width="1.6">
        <rect x="7" y="2" width="10" height="20" rx="2"/>
        <line x1="7" y1="5.5" x2="17" y2="5.5"/>
        <line x1="7" y1="18" x2="17" y2="18"/>
      </svg>
      <svg viewBox="0 0 24 24" fill="none" stroke="#1e1e1e" stroke-width="1.6">
        <rect x="2" y="5" width="20" height="14" rx="1"/>
        <path d="M2.5 5.5L12 13l9.5-7.5"/>
      </svg>
      <svg viewBox="0 0 24 24" fill="none" stroke="#1e1e1e" stroke-width="1.4">
        <circle cx="12" cy="12" r="10"/>
        <ellipse cx="12" cy="12" rx="4.5" ry="10"/>
        <line x1="2" y1="12" x2="22" y2="12"/>
        <path d="M4 6.5h16M4 17.5h16"/>
      </svg>
    </div>

    <ul class="contact-list">
      <li class="contact-phone">+971 5550192</li>
      <li class="contact-mobile">+971 555073</li>
      <li class="contact-email">q@k.example</li>
      <li class="contact-web">www.vastrelle.example</li>
    </ul>

    <div class="divider"></div>

    <div class="social-row">
      <span class="social-dot" aria-hidden="true"></span>
      <span class="social-handle">/vastrelle</span>
    </div>
  </section>
</main>
</body>
</html>
```